Quillmark Select

Letter Head, Envelope, Business Cards, Social Media Banner (FB/Twitter), Social Media Icon, Social Media Announcement Template...

We are a Softball Team/Organization

Target Market(s)

High School Student-Athletes (softball players) and their parents

Font styles to use
Serif

Requirements
Must have
• Logo & Colors
Must POP and say WOW
Common theme amongst all designs

```html
<!DOCTYPE html>
<html lang="en">
<head>
<meta charset="utf-8">
<title>Quillmark Select — Stationery Set</title>
<link href="https://fonts.googleapis.com/css2?family=Lato:wght@300;400;700;900&family=Allura&display=swap" rel="stylesheet">
<style>
  :root{
    --navy:#1e3762;
    --mist:#bfc6d3;
    --backdrop:#d8e4ef;
    --paper:#ffffff;
    --ink:#555a62;
    --ink-dark:#4b4f56;
    --on-navy:#ffffff;
    --logo-light:#c9d0de;
  }
  *{margin:0;padding:0;box-sizing:border-box}
  html,body{width:1200px;height:831px;overflow:hidden}
  body{background:var(--backdrop);font-family:'Lato',sans-serif;position:relative;color:var(--ink)}
  .sheet{position:absolute;background:var(--paper);box-shadow:0 2px 8px rgba(30,55,98,.25);overflow:hidden}
  .wave{position:absolute;left:0;top:0;width:100%}
  .brand{display:flex;align-items:center;gap:6px;position:absolute;font-family:'Lato',sans-serif;font-weight:900;color:var(--navy);letter-spacing:.02em;white-space:nowrap}
  .brand .dot{display:block;border-radius:50%;background:currentColor}
  .brand--light{color:var(--logo-light)}

  /* Letterhead */
  .letterhead{left:117px;top:111px;width:430px;height:609px}
  .letterhead .contact{position:absolute;right:41px;top:28px;text-align:right;color:var(--on-navy);font-size:8px;line-height:9.6px}
  .contact .gap{height:4px}
  .contact .row{display:flex;justify-content:flex-end;align-items:center;gap:8px;line-height:11px}
  .contact svg{width:8px;height:8px}
  .letterhead .brand{left:41px;top:132px;font-size:15px}
  .letterhead .brand .dot{width:12px;height:12px}
  .letter{position:absolute;left:41px;top:234px;width:349px}
  .letter .date{font-size:9.5px;font-weight:300;color:var(--ink)}
  .letter .name{font-size:14.5px;font-weight:900;color:var(--ink-dark);margin-top:5px;letter-spacing:.01em}
  .letter .role{font-size:10px;font-weight:300;margin-top:2px;color:var(--ink)}
  .letter .body{margin-top:26px;font-size:7.6px;line-height:15px;text-align:justify;font-weight:400;color:var(--ink)}
  .letter .body p+p{margin-top:15px}
  .letter .regards{margin-top:32px;font-size:9px;font-weight:400;color:var(--ink)}
  .letter .signature{font-family:'Allura',cursive;font-size:22px;color:var(--navy);margin-top:4px}

  /* Business card front */
  .card{width:182px;height:104px}
  .card-front{left:635px;top:113px}
  .card-front .person{position:absolute;right:19px;top:12px;text-align:right;color:var(--on-navy)}
  .person .who{font-size:8.5px;font-weight:900}
  .person .title{font-size:4.5px}
  .card-front .brand{left:12px;top:40px;font-size:8px;gap:4px}
  .card-front .brand .dot{width:7px;height:7px}
  .card-front .lines{position:absolute;left:10px;bottom:9px;font-size:4.4px;line-height:6.8px;color:var(--ink)}
  .lines .row{display:flex;align-items:center;gap:4px}
  .lines .ico{width:4px;height:4px;border-radius:1px;background:var(--navy)}
  .card-front .addr{position:absolute;right:11px;bottom:9px;font-size:4.4px;line-height:6.8px;text-align:right}
  .card-back{left:904px;top:111px;background:var(--navy)}
  .card-back .brand{left:50%;top:50%;transform:translate(-50%,-50%);font-size:11px}
  .card-back .brand .dot{width:9px;height:9px}

  /* Envelopes */
  .envelope{left:635px;width:451px}
  .envelope-back{top:248px;height:225px}
  .envelope-back .flap{position:absolute;left:0;top:0;width:100%;height:66px}
  .envelope-back .brand{left:50%;top:33px;transform:translate(-50%,-50%);font-size:11px}
  .envelope-back .brand .dot{width:9px;height:9px}
  .envelope-front{top:494px;height:226px}
  .envelope-front .addr{position:absolute;right:41px;top:21px;text-align:right;color:var(--on-navy);font-size:8px;line-height:9.5px;padding-right:6px;border-right:1px solid var(--on-navy)}
  .envelope-front .brand{left:44px;top:68px;font-size:15px}
  .envelope-front .brand .dot{width:12px;height:12px}
</style>
</head>
<body>

<!-- Letterhead -->
<section class="sheet letterhead">
  <svg class="wave" viewBox="0 0 430 125" height="125" preserveAspectRatio="none" aria-hidden="true">
    <path d="M0 0H430V101C398 112 370 118 332 118C262 118 205 82 145 56C100 37 40 36 0 52Z" fill="var(--navy)"/>
    <path d="M0 70C45 42 130 40 200 88C135 60 60 58 0 64Z" fill="var(--mist)"/>
    <path d="M48 28C120 14 172 40 240 74C300 104 340 118 378 120" fill="none" stroke="#fff" stroke-width="2.6"/>
  </svg>
  <div class="contact">
    <div>1450 Diamond Field Road</div>
    <div>Suite 200, Fairview TX</div>
    <div class="gap"></div>
    <div class="row">(555) 014-2290
      <svg viewBox="0 0 10 10"><path d="M2 1L4 3 3 4C4 6 5 7 6 7L7 6 9 8 8 9C4 9 1 6 1 2Z" fill="none" stroke="#fff" stroke-width="1"/></svg></div>
    <div class="row">info@quillmarkselect.com
      <svg viewBox="0 0 10 10"><rect x="1" y="2.5" width="8" height="5.5" fill="none" stroke="#fff" stroke-width="1"/><path d="M1 2.5L5 6 9 2.5" fill="none" stroke="#fff" stroke-width="1"/></svg></div>
    <div class="row">www.quillmarkselect.com
      <svg viewBox="0 0 10 10"><circle cx="5" cy="5" r="4" fill="none" stroke="#fff" stroke-width="1"/><path d="M1 5H9M5 1C3 3 3 7 5 9M5 1C7 3 7 7 5 9" fill="none" stroke="#fff" stroke-width=".7"/></svg></div>
  </div>
  <div class="brand"><span class="dot"></span>Quillmark Select</div>
  <article class="letter">
    <div class="date">01 December, 2021</div>
    <div class="name">CARLA BENTON</div>
    <div class="role">Cheif Executive Officer</div>
    <div class="body">
      <p>Contrary to popular belief, a strong season is not simply luck. It has roots in a long tradition of careful practice from day one, making each player better every week. Coach Elena Marsh, a veteran softball mentor at Brookhaven Prep Academy in Ohio, shaped one of the most respected training programs around.</p>
      <p>Our approach comes from sections 1.10.32 and 1.10.33 of "The Complete Infield Handbook" (The Rules of Fair and Steady Play) by Theo Lindqvist, written in 1985. This book is a treatise on the craft of fielding, very popular during the nineties. The first line of our playbook.</p>
      <p>The standard chunk of our playbook used since the 1990s is reproduced below for those interested.</p>
    </div>
    <div class="regards">Best Regards</div>
    <div class="signature">Benton</div>
  </article>
</section>

<!-- Business card front -->
<section class="sheet card card-front">
  <svg class="wave" viewBox="0 0 182 52" height="52" preserveAspectRatio="none" aria-hidden="true">
    <path d="M0 0H182V42C170 48 160 50 150 50C118 50 95 36 75 24C55 12 25 10 0 17Z" fill="var(--navy)"/>
    <path d="M0 27C22 15 55 14 85 36C58 22 28 21 0 25Z" fill="var(--mist)"/>
    <path d="M20 12C50 6 70 16 95 30C115 42 135 48 160 50" fill="none" stroke="#fff" stroke-width="1.3"/>
  </svg>
  <div class="person"><div class="who">DANA WHITFIELD</div><div class="title">Founder &amp; CEO</div></div>
  <div class="brand"><span class="dot"></span>Quillmark Select</div>
  <div class="lines">
    <div class="row"><span class="ico"></span>(555) 014-2290</div>
    <div class="row"><span class="ico"></span>info@quillmarkselect.com</div>
    <div class="row"><span class="ico"></span>www.quillmarkselect.com</div>
  </div>
  <div class="addr">1450 Diamond Field Road<br>Suite 200, Fairview TX</div>
</section>

<!-- Business card back -->
<section class="sheet card card-back">
  <div class="brand brand--light"><span class="dot"></span>Quillmark Select</div>
</section>

<!-- Envelope back -->
<section class="sheet envelope envelope-back">
  <svg class="flap" viewBox="0 0 451 66" preserveAspectRatio="none" aria-hidden="true">
    <path d="M0 0H451L447 40C445 56 434 66 418 66H33C17 66 6 56 4 40Z" fill="var(--navy)"/>
  </svg>
  <div class="brand brand--light"><span class="dot"></span>Quillmark Select</div>
</section>

<!-- Envelope front -->
<section class="sheet envelope envelope-front">
  <svg class="wave" viewBox="0 0 451 70" height="70" preserveAspectRatio="none" aria-hidden="true">
    <path d="M0 0H451V58C420 64 395 68 365 68C300 68 255 52 200 36C140 18 60 18 0 28Z" fill="var(--navy)"/>
    <path d="M0 40C70 22 150 22 210 50C150 32 70 30 0 36Z" fill="var(--mist)"/>
    <path d="M52 14C120 6 190 20 260 40C320 58 360 68 395 68" fill="none" stroke="#fff" stroke-width="2.2"/>
  </svg>
  <div class="addr">1450 Diamond Field Road<br>Suite 200, Fairview TX</div>
  <div class="brand"><span class="dot"></span>Quillmark Select</div>
</section>

</body>
</html>
```